Freelance film producer/editor wants you to gleam nova!

'Gleam Nova' is my production business based in Melbourne, though I do a fair bit of work overseas. I'm a one woman show most of the time but enlist other crew members for larger projects. I manage productions from start to finish including producing, filming, editing, distribution, photography and animation.

My current tag line and details are as follows:

Petra Vandoren
Producer. Editor. Thinker.
[M] +61 492 157 630
[E] pv[at]brightpanel.com.au
www.brightpanel.com.au

I have a fairly wicked sense of humour and love a good pun, so feel free to work this into your design!

The final designs should demonstrate the areas I work in but not limited to. I'd rather not use old and typical "film" looking elements such as a clapper or negative reel. Having said that, the logo itself (attached) is quite typical because the first 'o' is a closed aperture and the second is a wide aperture. Happy for the logo to be pulled apart for the business card to be more interesting.

The majority of projects I work on are quite different and in some cases a bit crazy. Lots of travel involved. The main difference between me and other producers is that I don't say I work in 'film', even though i do. I want the card to leave me open to new roles and projects as opposed to squashing myself into one particular category.

I'm open to colour but prefer a simple design that isn't too hectic.

I have also attached an example I did like that was printed on plastic but then I realised so many other people had ripped it off....

I'm open to paper board or plastic (transparent) designs etc. One sided or two sided.

Thanks for sharing your ideas with me and please, go as nuts as you want to with this! :)

Target Market(s)

My clients range from non profits in health and educational institutions to record labels and well known artists. The business attracts corporates as well though the majority of my business is achieved through referral and word of mouth so most people will soon realise that my personality and work are very much intertwined and the reason they hire me for a job.

Industry/Entity Type

Business

Font styles to use
Other font styles liked:
• Eurostile or similar

Requirements
Must have
• I have a very open mind when it comes to design. I do like the existing tag line but if you can come up with something better I'm all ears! (and eyes)

Nice to have
• Back of the business card can be graphics, there can be transparent elements or holes, embossing options...
Should not have
• Besides my name, nothing should scream "I am woman!" because in my industry that's not a selling point.

The colour pink is a definite no.

```html
<!DOCTYPE html>
<html lang="en">
<head>
<meta charset="utf-8">
<title>Gleam Nova — Business Card</title>
<link rel="stylesheet" href="https://fonts.googleapis.com/css2?family=Montserrat:wght@300;500;600;700&display=swap">
<style>
  :root {
    --backdrop: #2e2833;
    --card: #ebe3d1;
    --ink: #1c1a1b;
    --mark: #232122;
  }
  * { margin: 0; padding: 0; box-sizing: border-box; }
  html, body {
    width: 1027px;
    height: 1200px;
    overflow: hidden;
    background: var(--backdrop);
  }
  .canvas {
    position: relative;
    width: 1027px;
    height: 1200px;
  }
  .card {
    position: absolute;
    left: 303px;
    top: 372px;
    width: 421px;
    height: 734px;
    background: var(--card);
    color: var(--ink);
    font-family: "Montserrat", sans-serif;
  }
  .brand-dot {
    position: absolute;
    left: 155px;
    top: 206px;
  }
  .wordmark {
    position: absolute;
    right: 32px;
    top: 440px;
    font-size: 44px;
    font-weight: 300;
    letter-spacing: 0.5px;
    line-height: 1;
    white-space: nowrap;
    color: var(--ink);
  }
  .person {
    position: absolute;
    right: 30px;
    top: 544px;
    text-align: right;
  }
  .person-name {
    font-size: 27px;
    font-weight: 700;
    letter-spacing: 0.3px;
    text-transform: uppercase;
    line-height: 1.1;
    white-space: nowrap;
  }
  .person-role {
    margin-top: 4px;
    font-size: 15px;
    font-weight: 600;
  }
  .contact {
    position: absolute;
    right: 30px;
    top: 631px;
    text-align: right;
    font-size: 16px;
    font-weight: 600;
    font-style: normal;
    line-height: 27px;
    white-space: nowrap;
  }
  .contact .sep { padding: 0 3px; }
</style>
</head>
<body>
  <main class="canvas">
    <section class="card" aria-label="Business card">
      <svg class="brand-dot" width="204" height="204" viewBox="0 0 204 204" aria-hidden="true">
        <circle cx="102" cy="102" r="102" fill="var(--mark)"/>
      </svg>
      <div class="wordmark">gleam nova</div>
      <div class="person">
        <h1 class="person-name">Petra Vandoren</h1>
        <p class="person-role">Producer.Editor.Thinker</p>
      </div>
      <address class="contact">
        <div>+61 492 157 630<span class="sep">•</span>pv[at]brightpanel.com.au</div>
        <div>www.brightpanel.com.au</div>
      </address>
    </section>
  </main>
</body>
</html>
```